we need a business card in yellow, green and black with rounded edges. We are in the Construction and Engineering business. I need the below info included:

Neil Barton
Summitrow Engineering & Construction, Inc.
4158 Harbor Vale Drive,
Larkmont, CA 90817
714-555-0147 Office
714-555-0192 Cell
714-555-0163 Fax
nb@summitrowec.com

thanks for your help!

```html
<!DOCTYPE html>
<html lang="en">
<head>
<meta charset="utf-8">
<title>Summitrow Engineering &amp; Construction – Business Card</title>
<link rel="stylesheet" href="https://fonts.googleapis.com/css2?family=Open+Sans:wght@600;700&display=swap">
<style>
  :root {
    --bg: #e9e7e3;
    --card: #ffffff;
    --green: #2aa84a;
    --yellow: #e3e532;
    --black: #111111;
    --ink: #1c1c1c;
  }
  * { box-sizing: border-box; margin: 0; padding: 0; }
  html, body { width: 1200px; height: 1000px; overflow: hidden; }
  body {
    background: var(--bg);
    position: relative;
    font-family: "Open Sans", Arial, sans-serif;
    color: var(--ink);
  }
  .card {
    position: absolute;
    left: 250px;
    width: 700px;
    height: 400px;
    background: var(--card);
    border-radius: 26px;
    overflow: hidden;
    box-shadow: 0 10px 28px rgba(0,0,0,0.18);
  }
  .card--front { top: 70px; }
  .card--back { top: 530px; }

  .edge-stripe {
    position: absolute;
    left: 0; right: 0; bottom: 0;
    height: 12px;
    display: flex;
  }
  .edge-stripe .seg-green { flex: 0 0 38%; background: var(--green); }
  .edge-stripe .seg-yellow { flex: 0 0 34%; background: var(--yellow); }
  .edge-stripe .seg-black { flex: 1; background: var(--black); }

  .company {
    display: flex;
    align-items: center;
    gap: 12px;
  }
  .company__square {
    width: 16px; height: 16px;
    background: var(--green);
    flex: none;
  }
  .company__name {
    font-family: "Open Sans", Arial, sans-serif;
    font-weight: 700;
    color: var(--ink);
    white-space: nowrap;
  }

  .card--front .company {
    position: absolute;
    left: 0; right: 0; top: 180px;
    justify-content: center;
  }
  .card--front .company__name { font-size: 24px; }
  .card--front .company__square { width: 20px; height: 20px; }

  .card--back .company {
    position: absolute;
    left: 56px; top: 70px;
  }
  .card--back .company__name { font-size: 17px; }

  .person {
    position: absolute;
    left: 56px; top: 148px;
    font-size: 28px;
    font-weight: 700;
    letter-spacing: 1px;
    text-transform: uppercase;
    color: var(--green);
  }
  .contacts {
    position: absolute;
    left: 56px; top: 204px;
    list-style: none;
    font-size: 17px;
    font-weight: 600;
    line-height: 27px;
  }
  .contacts .label { color: var(--green); margin-right: 6px; }
</style>
</head>
<body>
  <section class="card card--front" aria-label="Card front">
    <div class="company">
      <span class="company__square"></span>
      <span class="company__name">Summitrow Engineering &amp; Construction, Inc.</span>
    </div>
    <div class="edge-stripe"><span class="seg-green"></span><span class="seg-yellow"></span><span class="seg-black"></span></div>
  </section>

  <section class="card card--back" aria-label="Card back">
    <div class="company">
      <span class="company__square"></span>
      <span class="company__name">Summitrow Engineering &amp; Construction, Inc.</span>
    </div>
    <h1 class="person">Neil Barton</h1>
    <ul class="contacts">
      <li><span class="label">P:</span>714-555-0147</li>
      <li><span class="label">M:</span>714-555-0192</li>
      <li><span class="label">F:</span>714-555-0163</li>
      <li><span class="label">E:</span>nb@summitrowec.com</li>
      <li><span class="label">A:</span>4158 Harbor Vale Drive, Larkmont, CA 90817</li>
    </ul>
    <div class="edge-stripe"><span class="seg-green"></span><span class="seg-yellow"></span><span class="seg-black"></span></div>
  </section>
</body>
</html>
```